Design a custom Workvine Background Banner (JPG, GIF or PNG)

Hello,
I would like a customized background for my Workvine profile. The specifications are as follows:

* File type JPG, GIF or PNG
* No larger than 4MB.
* Pixel dimensions between 1000 X 425 and 4000 X 4000

Workvine provides these further instructions:

If your background image appears blurry or pixelated, please choose an image with a file size as close to the maximum as possible, as images with larger file sizes typically look better. Photos will also look better than images with logos. If your image is still blurry or pixelated, you may want to run it through a compression tool such as Trimage for Windows or ImageOptim for Mac before uploading it to Workvine.

I want a banner that emphasizes that I'm a healthcare CIO and lists the following responsibilities:

HIPAA
Revenue Cycle
EHR
Health IT
ICD-10
Meaningful Use
Integration
Strategy
Security

Let me know if there isn't enough room for all of these and I can pare it down. I'm attaching two examples of how others in my profession have done that. I'm also including my current banner (which I like) and would be great if we somehow incorporate into the design. No worries if we can't.

Target Market(s)

Recruiters and my peers that may be viewing my profile.

Font styles to use
Sans Serif

Requirements
Nice to have
• Would love to incorporate the blue computer vector image that I attached.

```html
<!DOCTYPE html>
<html lang="en">
<head>
<meta charset="utf-8">
<title>Healthcare CIO Profile Banner</title>
<link rel="stylesheet" href="https://fonts.googleapis.com/css2?family=Open+Sans:wght@400&display=swap">
<style>
  :root {
    --bg-deep: #4f8fae;
    --bg-mid: #6eaecb;
    --bg-light: #93cde0;
    --green: #1e6a2c;
    --red: #c8432c;
    --purple: #4b4d98;
    --teal-dark: #163f4f;
    --gold: #b3ab6b;
  }
  html, body {
    margin: 0;
    padding: 0;
    overflow: hidden;
    background: #ffffff;
  }
  .banner {
    position: relative;
    width: 1200px;
    height: 510px;
    overflow: hidden;
    font-family: "Open Sans", Arial, sans-serif;
    font-weight: 400;
  }
  .banner__backdrop {
    position: absolute;
    inset: 0;
    background:
      linear-gradient(90deg, rgba(255,255,255,0) 0%, rgba(255,255,255,0.12) 45%, rgba(255,255,255,0) 70%, rgba(255,255,255,0.1) 100%),
      linear-gradient(180deg, var(--bg-mid) 0%, var(--bg-light) 55%, var(--bg-deep) 100%);
  }
  .tag {
    position: absolute;
    margin: 0;
    white-space: nowrap;
    line-height: 1;
    transform: translate(-50%, -50%) rotate(var(--rot, 0deg));
  }
  .tag--green { color: var(--green); }
  .tag--red { color: var(--red); }
  .tag--purple { color: var(--purple); }
  .tag--teal { color: var(--teal-dark); }
  .tag--gold { color: var(--gold); }
  .tag--faint { opacity: 0.45; }
  .tag--soft { opacity: 0.7; }
</style>
</head>
<body>
<main class="banner">
  <div class="banner__backdrop" role="img" aria-label="Blue background of falling binary code columns"></div>

  <p class="tag tag--red tag--faint" style="left:168px;top:90px;font-size:41px;--rot:4deg">ICD-10</p>
  <p class="tag tag--green tag--soft" style="left:458px;top:70px;font-size:24px">EHR</p>
  <p class="tag tag--purple tag--faint" style="left:556px;top:82px;font-size:20px;--rot:40deg">Security</p>
  <p class="tag tag--gold tag--faint" style="left:756px;top:55px;font-size:20px">Meaningful Use</p>
  <p class="tag tag--red" style="left:928px;top:94px;font-size:54px">Integration</p>
  <p class="tag tag--red tag--soft" style="left:1116px;top:162px;font-size:56px;--rot:-90deg">ICD-10</p>
  <p class="tag tag--green" style="left:228px;top:146px;font-size:50px;--rot:-15deg">Revenue Cycle</p>
  <p class="tag tag--green tag--faint" style="left:509px;top:138px;font-size:44px">EHR</p>
  <p class="tag tag--purple" style="left:684px;top:118px;font-size:22px">Health IT</p>
  <p class="tag tag--purple tag--faint" style="left:1020px;top:186px;font-size:17px;--rot:55deg">Health IT</p>
  <p class="tag tag--teal" style="left:872px;top:192px;font-size:36px;--rot:-15deg">HIPAA</p>
  <p class="tag tag--gold tag--faint" style="left:342px;top:194px;font-size:22px">Meaningful Use</p>
  <p class="tag tag--teal" style="left:518px;top:224px;font-size:84px;--rot:-18deg">HIPAA</p>
  <p class="tag tag--purple" style="left:895px;top:271px;font-size:56px">Health IT</p>
  <p class="tag tag--red tag--faint" style="left:130px;top:274px;font-size:22px">Integration</p>
  <p class="tag tag--purple tag--faint" style="left:342px;top:286px;font-size:18px;--rot:50deg">Security</p>
  <p class="tag tag--green" style="left:571px;top:308px;font-size:40px">EHR</p>
  <p class="tag tag--purple tag--faint" style="left:538px;top:378px;font-size:56px;--rot:48deg">Security</p>
  <p class="tag tag--purple tag--faint" style="left:654px;top:336px;font-size:72px;--rot:-90deg">ICD-10</p>
  <p class="tag tag--red" style="left:144px;top:360px;font-size:58px;--rot:-33deg">Strategy</p>
  <p class="tag tag--green" style="left:336px;top:394px;font-size:48px">EHR</p>
  <p class="tag tag--green" style="left:194px;top:414px;font-size:11px;--rot:-8deg">Revenue Cycle</p>
  <p class="tag tag--green" style="left:248px;top:454px;font-size:30px;--rot:-15deg">Revenue Cycle</p>
  <p class="tag tag--red" style="left:460px;top:458px;font-size:22px">Integration</p>
  <p class="tag tag--gold tag--soft" style="left:878px;top:444px;font-size:56px">Meaningful Use</p>
  <p class="tag tag--red tag--faint" style="left:806px;top:374px;font-size:20px;--rot:-15deg">Strategy</p>
  <p class="tag tag--purple" style="left:900px;top:364px;font-size:20px">Health IT</p>
  <p class="tag tag--teal" style="left:1042px;top:366px;font-size:32px;--rot:-18deg">HIPAA</p>
  <p class="tag tag--purple tag--faint" style="left:1134px;top:372px;font-size:24px;--rot:90deg">Security</p>
</main>
</body>
</html>
```